Business Card Design Project

Construction

Industry/Entity Type

Business

I've had the same logo for about 5 years. The logo itself is fine, however I'm looking to get a new design on the card. The green for the log is fine but the grey for the rest of the card is kind of dark and blah. Would like a new look. I'll send the file with the logo.

```html
<!DOCTYPE html>
<html lang="en">
<head>
<meta charset="utf-8">
<title>Brightline Commercial Builders – Business Cards</title>
<link href="https://fonts.googleapis.com/css2?family=Open+Sans:wght@400;600;700&display=swap" rel="stylesheet">
<style>
  :root{
    --stage:#b3b6b4;
    --carbon-light:#232725;
    --carbon-dark:#0b0c0c;
    --green:#1e9a4a;
    --green-bright:#3fbf6c;
    --green-text:#2fb35c;
    --white:#f4f5f4;
    --ink:#111312;
    --muted:#d9dcda;
  }
  *{box-sizing:border-box;margin:0;padding:0}
  html,body{width:1200px;height:900px;overflow:hidden;background:var(--stage);
    font-family:"Open Sans",Arial,sans-serif}
  .canvas{position:relative;width:1200px;height:900px}
  .card{position:absolute;width:700px;height:400px;border-radius:22px;overflow:hidden;
    box-shadow:0 14px 30px rgba(0,0,0,.35)}
  .card--back{left:440px;top:50px;
    background:radial-gradient(ellipse at 35% 30%,var(--carbon-light),var(--carbon-dark) 80%)}
  .card--front{left:60px;top:460px;background:var(--white)}
  .card-shapes{position:absolute;inset:0}
  .abs{position:absolute}
  .brand{display:flex;align-items:center;gap:12px}
  .brand-mark{width:22px;height:22px;background:var(--green)}
  .brand-name{font-weight:700;font-size:30px;letter-spacing:1px;line-height:1.05}
  .brand-sub{font-weight:700;font-size:13px;letter-spacing:3px;margin-top:4px}

  /* back card */
  .back-brand{left:70px;top:90px;color:var(--white)}
  .back-brand .brand-name,.back-brand .brand-sub{color:var(--white)}
  .website{left:70px;top:200px;color:var(--muted);font-size:15px;letter-spacing:.5px}
  .services{left:390px;top:70px;list-style:none;color:var(--muted);font-size:17px;line-height:1.65}
  .services li{display:flex;align-items:center;gap:8px}
  .tick{width:16px;height:14px}
  .naics{left:390px;top:232px;color:var(--muted);font-size:16px;line-height:1.6}
  .back-license{left:390px;top:330px;color:var(--muted);font-size:16px}

  /* front card */
  .person{left:40px;top:40px}
  .person-name{color:var(--white);font-size:24px;font-weight:600;letter-spacing:.5px}
  .person-role{color:var(--green-text);font-size:15px;margin-top:2px}
  .contact{left:40px;top:170px;list-style:none;color:var(--white);font-size:16px;line-height:1.9}
  .contact li{display:flex;align-items:center;gap:10px}
  .icon{width:18px;height:16px}
  .service-area{left:40px;top:283px;color:var(--white);font-size:19px}
  .front-brand{left:440px;top:110px;color:var(--ink)}
  .front-brand .brand-name,.front-brand .brand-sub{color:var(--ink)}
  .seal{left:575px;top:215px;width:72px;height:72px;border-radius:50%;
    background:radial-gradient(circle,#d8d6c4,#a9a68f);box-shadow:0 2px 4px rgba(0,0,0,.25)}
  .front-license{left:430px;top:320px;color:var(--white);font-size:22px}
</style>
</head>
<body>
<main class="canvas">

  <section class="card card--back" aria-label="Back of business card">
    <div class="abs brand back-brand">
      <span class="brand-mark"></span>
      <div>
        <div class="brand-name">BRIGHTLINE</div>
        <div class="brand-sub">COMMERCIAL BUILDERS</div>
      </div>
    </div>
    <p class="abs website">BRIGHTLINECOMMERCIAL.com</p>
    <ul class="abs services">
      <li><svg class="tick" viewBox="0 0 16 14"><path d="M1 7l5 5L15 1" fill="none" stroke="#2fb35c" stroke-width="3"/></svg>A-Genral Engineering</li>
      <li><svg class="tick" viewBox="0 0 16 14"><path d="M1 7l5 5L15 1" fill="none" stroke="#2fb35c" stroke-width="3"/></svg>B-Genral Building</li>
      <li><svg class="tick" viewBox="0 0 16 14"><path d="M1 7l5 5L15 1" fill="none" stroke="#2fb35c" stroke-width="3"/></svg>C21 Demo/Bldg. Moving</li>
      <li><svg class="tick" viewBox="0 0 16 14"><path d="M1 7l5 5L15 1" fill="none" stroke="#2fb35c" stroke-width="3"/></svg>C36 Plumbing</li>
    </ul>
    <p class="abs naics">NAICS CODES<br>236220, 238110, 236118, 23810,<br>238350, 238390, 327320</p>
    <p class="abs back-license">License 2046718</p>
  </section>

  <section class="card card--front" aria-label="Front of business card">
    <svg class="card-shapes" viewBox="0 0 700 400" preserveAspectRatio="none" aria-hidden="true">
      <defs>
        <radialGradient id="carbon" cx="30%" cy="30%" r="80%">
          <stop offset="0" stop-color="#232725"/><stop offset="1" stop-color="#0b0c0c"/>
        </radialGradient>
      </defs>
      <polygon points="0,0 410,0 340,400 0,400" fill="url(#carbon)"/>
      <polygon points="420,0 438,0 368,400 350,400" fill="#1e9a4a"/>
      <rect x="0" y="268" width="375" height="50" fill="#3fbf6c"/>
      <polygon points="375,300 700,300 700,355 366,355" fill="#1e9a4a"/>
    </svg>

    <div class="abs person">
      <h1 class="person-name">MARCUS HALE</h1>
      <p class="person-role">PMP &nbsp;|&nbsp; President</p>
    </div>
    <ul class="abs contact">
      <li><svg class="icon" viewBox="0 0 18 14"><rect x="1" y="1" width="16" height="12" fill="none" stroke="#2fb35c" stroke-width="2"/><path d="M1 1l8 7 8-7" fill="none" stroke="#2fb35c" stroke-width="2"/></svg>marcus@brightlinecommercial.com</li>
      <li><svg class="icon" viewBox="0 0 18 16"><path d="M2 5c0-3 14-3 14 0v2h-4V5H6v2H2z M4 8h10l2 7H2z" fill="#2fb35c"/></svg>(310) 555-0148</li>
    </ul>
    <p class="abs service-area">Serving All of Southern California</p>

    <div class="abs brand front-brand">
      <span class="brand-mark"></span>
      <div>
        <div class="brand-name">BRIGHTLINE</div>
        <div class="brand-sub">COMMERCIAL BUILDERS</div>
      </div>
    </div>
    <div class="abs seal" role="img" aria-label="Service anniversary seal"></div>
    <p class="abs front-license">License: 2046718</p>
  </section>

</main>
</body>
</html>
```